Business cards and stationary
Venoki Imaging, llc
Professional
Miriam Colfax. Dana Pruitt
Owners
17 Harrow Lane
Bloomingburg, ny 12721 (Miriam )
52 Willowby Road
New Windsor, NY 12553 ( Dana )
Miriam 914-555-0142. /. Dana 845-555-0197
Juniper41@mailvex.com

```html
<!DOCTYPE html>
<html lang="en">
<head>
<meta charset="utf-8">
<title>Venoki Imaging, llc – Stationery</title>
<link href="https://fonts.googleapis.com/css2?family=Montserrat:wght@400;500&display=swap" rel="stylesheet">
<style>
  :root {
    --bg: #ececec;
    --paper: #ffffff;
    --blue: #1c5a9c;
    --deep-blue: #123f78;
    --purple: #8a2a8e;
    --cyan: #2bb3d8;
    --ink: #2a4f86;
    --muted: #7a7f88;
    --band: linear-gradient(90deg, var(--deep-blue) 0%, var(--blue) 35%, var(--purple) 100%);
  }
  * { margin: 0; padding: 0; box-sizing: border-box; }
  html, body { width: 1200px; height: 936px; overflow: hidden; background: var(--bg); }
  body { position: relative; font-family: "Montserrat", Arial, sans-serif; }

  .sheet { position: absolute; background: var(--paper); box-shadow: 0 2px 6px rgba(0,0,0,.18); overflow: hidden; }

  .brand { display: flex; flex-direction: column; align-items: flex-start; }
  .brand-row { display: flex; align-items: center; gap: 8px; }
  .brand-dot { border-radius: 50%; background: var(--purple); flex: none; }
  .brand-name { font-family: "Montserrat", Arial, sans-serif; font-weight: 500; color: var(--ink); white-space: nowrap; letter-spacing: 0; }
  .brand-tag { font-family: "Montserrat", Arial, sans-serif; font-weight: 400; color: var(--muted); letter-spacing: .25em; text-transform: uppercase; white-space: nowrap; }

  .band { position: absolute; left: 0; right: 0; background: var(--band); }
  .band::before { content: ""; position: absolute; left: 0; right: 0; top: -3px; height: 3px; background: var(--cyan); opacity: .8; }
  .band-domain { position: absolute; right: 18px; top: 50%; transform: translateY(-50%); color: #fff; font-size: 9px; letter-spacing: .2em; text-transform: uppercase; white-space: nowrap; }

  .contact { position: absolute; font-size: 8px; color: var(--muted); line-height: 1.6; white-space: nowrap; }
  .contact span::before { content: "●"; color: var(--purple); margin-right: 4px; font-size: 6px; }

  /* letterhead */
  .letterhead { left: 183px; top: 63px; width: 388px; height: 551px; }
  .letterhead .top-band { top: 10px; height: 22px; }
  .letterhead .brand { position: absolute; left: 62px; top: 54px; }
  .letterhead .contact { right: 40px; top: 52px; }
  .letterhead .bottom-band { bottom: 0; height: 34px; }

  /* cover sheet */
  .cover { left: 634px; top: 41px; width: 464px; height: 573px; }
  .cover .brand { position: absolute; left: 0; right: 0; top: 250px; align-items: center; }
  .cover .bottom-band { bottom: 0; height: 36px; }

  /* business cards */
  .card { width: 203px; height: 96px; left: 43px; }
  .card-front { top: 662px; }
  .card-front .brand { position: absolute; left: 10px; top: 12px; }
  .card-front .band { top: 42px; left: 80px; height: 22px; }
  .card-front .card-person { position: absolute; left: 90px; top: 49px; color: #fff; font-size: 7px; white-space: nowrap; }
  .card-front .card-lines { position: absolute; left: 90px; top: 70px; font-size: 6px; color: var(--muted); line-height: 1.5; white-space: nowrap; }
  .card-back { top: 779px; height: 121px; }
  .card-back .brand { position: absolute; left: 16px; top: 36px; }
  .card-back .band { bottom: 16px; left: 80px; height: 10px; }

  /* envelope front */
  .envelope { left: 264px; top: 665px; width: 434px; height: 218px; }
  .envelope .brand { position: absolute; left: 22px; top: 28px; }
  .envelope .contact { left: 22px; top: 76px; }
  .envelope .bottom-band { bottom: 16px; height: 24px; }

  /* envelope back */
  .envelope-back { left: 738px; top: 665px; width: 424px; height: 218px; }
  .envelope-back .flap { position: absolute; left: 0; top: 0; width: 100%; height: 74px; }
  .envelope-back .flap-domain { position: absolute; left: 0; right: 0; top: 26px; text-align: center; color: #fff; font-size: 9px; letter-spacing: .25em; text-transform: uppercase; }
</style>
</head>
<body>

<section class="sheet letterhead">
  <div class="band top-band"></div>
  <div class="brand">
    <div class="brand-row"><span class="brand-dot" style="width:14px;height:14px"></span><span class="brand-name" style="font-size:12px">Venoki Imaging, llc</span></div>
    <span class="brand-tag" style="font-size:6px;margin:3px 0 0 22px">Mobile Ultrasound</span>
  </div>
  <div class="contact">
    <span>914-555-0142</span><br>
    <span>845-555-0197</span><br>
    <span>Juniper41@mailvex.com</span>
  </div>
  <div class="band bottom-band"><span class="band-domain">www.VenokiImaging.com</span></div>
</section>

<section class="sheet cover">
  <div class="brand">
    <div class="brand-row"><span class="brand-dot" style="width:24px;height:24px"></span><span class="brand-name" style="font-size:24px">Venoki Imaging, llc</span></div>
    <span class="brand-tag" style="font-size:10px;margin-top:8px">Mobile Ultrasound</span>
  </div>
  <div class="band bottom-band"><span class="band-domain">www.VenokiImaging.com</span></div>
</section>

<section class="sheet card card-front">
  <div class="brand">
    <div class="brand-row"><span class="brand-dot" style="width:10px;height:10px"></span><span class="brand-name" style="font-size:8px">Venoki Imaging</span></div>
  </div>
  <div class="band"></div>
  <div class="card-person">Miriam Colfax · Owner</div>
  <div class="card-lines">914-555-0142<br>Juniper41@mailvex.com</div>
</section>

<section class="sheet card card-back">
  <div class="brand">
    <div class="brand-row"><span class="brand-dot" style="width:16px;height:16px"></span><span class="brand-name" style="font-size:11px">Venoki Imaging, llc</span></div>
    <span class="brand-tag" style="font-size:5px;margin:3px 0 0 24px">Mobile Ultrasound</span>
  </div>
  <div class="band"></div>
</section>

<section class="sheet envelope">
  <div class="brand">
    <div class="brand-row"><span class="brand-dot" style="width:14px;height:14px"></span><span class="brand-name" style="font-size:12px">Venoki Imaging, llc</span></div>
    <span class="brand-tag" style="font-size:6px;margin:3px 0 0 22px">Mobile Ultrasound</span>
  </div>
  <div class="contact">914-555-0142</div>
  <div class="band bottom-band"><span class="band-domain">www.VenokiImaging.com</span></div>
</section>

<section class="sheet envelope-back">
  <svg class="flap" viewBox="0 0 424 74" preserveAspectRatio="none" aria-hidden="true">
    <defs>
      <linearGradient id="flapFill" x1="0" x2="1">
        <stop offset="0" stop-color="#123f78"/>
        <stop offset="1" stop-color="#1c5a9c"/>
      </linearGradient>
    </defs>
    <path d="M0 0 H424 V58 Q212 80 0 58 Z" fill="url(#flapFill)"/>
  </svg>
  <div class="flap-domain">www.VenokiImaging.com</div>
</section>

</body>
</html>
```